Design for Viral Content Website

In need of a webdesign for a website with mostly Buzzlane. There are three versions of a landingpage:
a) Whole article on one page
b) Article split into several pages each with image and previous/next buttons
c) Mobile version
I uploaded very rough versions of how it should look like. Don't judge me, if I would be a designer, I'd do it myself ;)
Don't have a mockup for the index/category listing, surprise me :)
The header must be small (as here on tandemlyx) because it will be fixed and scroll when the user scrolls down.
4 page

```html
<!DOCTYPE html>
<html lang="en">
<head>
<meta charset="utf-8">
<title>Buzzlane</title>
<link href="https://fonts.googleapis.com/css2?family=Raleway:wght@400;500;600;700&display=swap" rel="stylesheet">
<style>
:root{
  --brand:#3d55a8;
  --brand-soft:#4a63b5;
  --ink:#222;
  --muted:#9a9a9a;
  --page:#efefef;
  --card:#fff;
  --nav:#2b2b2b;
  --share-main:#3b5998;
  --share-chirp:#3fa9e0;
  --share-circle:#dd4b39;
  --share-thread:#ff4500;
  --share-board:#cb2027;
  --share-work:#2d64a8;
  --share-wander:#4cb050;
  --tube:#e02a20;
}
*{margin:0;padding:0;box-sizing:border-box}
html,body{width:891px;height:1200px;overflow:hidden}
body{background:var(--page);font-family:'Raleway',sans-serif;color:var(--ink);position:relative}
.abs{position:absolute}
.site-header{left:0;top:0;width:891px;height:64px;background:var(--card)}
.site-name{left:55px;top:12px;font-size:34px;font-weight:700;color:var(--brand);letter-spacing:-.5px}
.social-tile{top:22px;width:25px;height:25px;border-radius:4px}
.like-btn{left:734px;top:22px;width:58px;height:25px;background:var(--share-main);color:#fff;font-size:13px;font-weight:600;border-radius:3px;display:flex;align-items:center;justify-content:center}
.like-count{left:797px;top:22px;width:35px;height:25px;border:1px solid #aaa;border-radius:3px;font-size:12px;display:flex;align-items:center;justify-content:center;color:#444;background:#fff}
.main-nav{left:0;top:65px;width:891px;height:37px;background:var(--nav);display:flex;justify-content:center;align-items:center;gap:24px}
.main-nav a{color:#eee;text-decoration:none;font-size:11.5px;font-weight:500}
.trending{top:111px;width:122px}
.trending .ph{width:122px;height:68px}
.trending p{font-size:11.5px;margin-top:6px;color:#333;font-weight:500}
.share{top:213px;height:44px;color:#fff;display:flex;align-items:center;justify-content:center;font-size:10px;font-weight:700;border-radius:2px}
.share.narrow{width:43px;font-size:8px}
.panel{background:var(--card)}
.article-title{left:55px;top:267px;width:517px;height:119px;font-size:27px;line-height:33px;text-align:center;font-weight:500;display:flex;align-items:center;justify-content:center}
.slide{left:55px;top:397px;width:517px;height:371px}
.slide h2{position:absolute;left:10px;top:7px;font-size:17px;font-weight:400;color:var(--brand)}
.slide .lede{position:absolute;left:10px;top:35px;width:490px;font-size:9.5px;line-height:10.5px}
.slide .ph{position:absolute;left:10px;top:71px;width:497px;height:270px}
.slide .credit{position:absolute;left:12px;top:350px;font-size:9.5px;color:var(--muted)}
.pager{top:780px;font-size:13px;color:var(--brand);display:flex;align-items:center;gap:5px;font-weight:500}
.pager .box{width:21px;height:21px;border:1.5px solid var(--brand);border-radius:3px}
.count{left:280px;top:782px;width:70px;text-align:center;font-size:12.5px;color:#333}
.grid{left:55px;top:813px;width:517px;height:331px}
.tile{position:absolute;width:160px}
.tile .ph{height:118px}
.tile p{font-size:12.5px;margin-top:5px;font-weight:500}
.show-more{left:260px;top:1160px;width:110px;text-align:center;font-size:11.5px;color:var(--brand)}
.sidebar{left:582px;top:213px;width:252px;height:801px}
.sidebar-head{position:absolute;left:8px;top:9px;width:236px;height:30px;background:var(--brand-soft);color:#fff;font-size:11.5px;padding-left:8px;display:flex;align-items:center}
.rec{position:absolute;left:8px;width:236px}
.rec .ph{height:126px}
.rec h3{font-size:12.5px;font-weight:500;margin-top:7px}
.rec .meta{display:flex;justify-content:space-between;font-size:6.5px;color:#b0b0b0;margin-top:7px}
.newsletter{left:582px;top:1026px;width:252px;height:118px;background:var(--brand-soft);color:#fff;text-align:center}
.newsletter h4{font-size:12.5px;font-weight:500;margin-top:16px}
.newsletter p{font-size:8.5px;line-height:10.5px;margin-top:7px}
.newsletter .field{position:absolute;left:11px;top:83px;width:164px;height:17px;border-bottom:1px solid #8b9bd2;font-size:9px;color:#8b9bd2;text-align:left;padding-left:1px}
.newsletter .submit{position:absolute;left:182px;top:79px;width:61px;height:21px;background:#fff;color:var(--brand);font-size:10px;display:flex;align-items:center;justify-content:center}
.footer{left:600px;top:1162px;width:260px;text-align:center;font-size:8.5px;line-height:12px;color:#333}
.footer span{margin:0 3px}
</style>
</head>
<body>
<header class="abs site-header">
  <div class="abs site-name">Buzzlane</div>
  <div class="abs social-tile" style="left:644px;background:var(--share-main)" role="img" aria-label="Friendbook"></div>
  <div class="abs social-tile" style="left:672px;background:var(--share-chirp)" role="img" aria-label="Chirper"></div>
  <div class="abs social-tile" style="left:701px;background:var(--tube)" role="img" aria-label="ViewTube"></div>
  <div class="abs like-btn">Like</div>
  <div class="abs like-count">60k</div>
</header>
<nav class="abs main-nav">
  <a>HOMEPAGE</a><a>VIRAL</a><a>PAGELINK</a>
  <a>PAGELINK <svg width="7" height="5" viewBox="0 0 7 5"><path d="M1 1l2.5 2.5L6 1" stroke="#eee" fill="none"/></svg></a>
  <a>PAGELINK</a><a>ABOUT US</a><a>PRIVACY POLICY</a><a>CONTACT US</a>
</nav>

<div class="abs trending" style="left:58px"><div class="ph" style="background:linear-gradient(#2a2a2a,#514c48)" role="img" aria-label="Guests at an evening event"></div><p>Article title here</p></div>
<div class="abs trending" style="left:189px"><div class="ph" style="background:linear-gradient(#6ea3d6,#c9c0b3)" role="img" aria-label="Frowning cat"></div><p>Article title here</p></div>
<div class="abs trending" style="left:319px"><div class="ph" style="background:linear-gradient(#d7d9dc,#6d8a4a)" role="img" aria-label="Cheerleaders on a field"></div><p>Article title here</p></div>
<div class="abs trending" style="left:450px"><div class="ph" style="background:linear-gradient(#5f5548,#9e8772)" role="img" aria-label="Babies in knitted hats"></div><p>Article title here</p></div>
<div class="abs trending" style="left:580px"><div class="ph" style="background:linear-gradient(#c9c6c3,#3a3534)" role="img" aria-label="Wedding couple"></div><p>Article title here</p></div>
<div class="abs trending" style="left:710px"><div class="ph" style="background:linear-gradient(#b7aa9c,#8d6c5c)" role="img" aria-label="Before and after fitness"></div><p>Article title here</p></div>

<div class="abs share" style="left:55px;width:193px;background:var(--share-main)">SHARE</div>
<div class="abs share narrow" style="left:259px;background:var(--share-chirp)">CHIRP</div>
<div class="abs share narrow" style="left:313px;background:var(--share-circle)">CIRCLE</div>
<div class="abs share narrow" style="left:366px;background:var(--share-thread)">THREAD</div>
<div class="abs share narrow" style="left:421px;background:var(--share-board)">BOARD</div>
<div class="abs share narrow" style="left:474px;background:var(--share-work)">WORK</div>
<div class="abs share narrow" style="left:528px;background:var(--share-wander)">WANDER</div>

<h1 class="abs panel article-title">Title of this article will be goes here,<br>how many line you want no issue<br>the numbers of lines.</h1>

<section class="abs panel slide">
  <h2>Image #1 Title will be here</h2>
  <p class="lede">Lorem Ipsum is simply dummy text of the printing and typesetting industry. Lorem Ipsum has been the industry's standard dummy text ever since the 1500s</p>
  <div class="ph" style="background:linear-gradient(135deg,#b98a5e,#3a2f28 55%,#6b5140)" role="img" aria-label="Group of friends at a party"></div>
  <p class="credit">via picshare</p>
</section>

<div class="abs pager" style="left:56px"><svg class="box" viewBox="0 0 21 21"><path d="M12 6l-4 4.5 4 4.5" stroke="#3d55a8" stroke-width="1.5" fill="none"/></svg>Previous</div>
<div class="abs count">5 / 50</div>
<div class="abs pager" style="left:519px">Next<svg class="box" viewBox="0 0 21 21"><path d="M9 6l4 4.5-4 4.5" stroke="#3d55a8" stroke-width="1.5" fill="none"/></svg></div>

<section class="abs panel grid">
  <div class="tile" style="left:11px;top:13px"><div class="ph" style="background:linear-gradient(#d8d8d6,#7f7b76)" role="img" aria-label="Cat in a costume"></div><p>Article title will be here.</p></div>
  <div class="tile" style="left:179px;top:13px"><div class="ph" style="background:linear-gradient(#9b8373,#d7b8a5)" role="img" aria-label="Newborn feet"></div><p>Article title will be here.</p></div>
  <div class="tile" style="left:348px;top:13px"><div class="ph" style="background:linear-gradient(#8fa3b6,#dfe7ec)" role="img" aria-label="Frozen lighthouse pier"></div><p>Article title will be here.</p></div>
  <div class="tile" style="left:11px;top:176px"><div class="ph" style="background:linear-gradient(#3d2b25,#8e3a30)" role="img" aria-label="Group selfie at an awards show"></div><p>Article title will be here.</p></div>
  <div class="tile" style="left:179px;top:176px"><div class="ph" style="background:linear-gradient(#a5563c,#4a6a54)" role="img" aria-label="Bucket of water poured over a man"></div><p>Article title will be here.</p></div>
  <div class="tile" style="left:348px;top:176px"><div class="ph" style="background:linear-gradient(#54585c,#d9d7d3)" role="img" aria-label="Singer on stage"></div><p>Article title will be here.</p></div>
</section>
<div class="abs show-more">Show More<br><svg width="9" height="6" viewBox="0 0 9 6"><path d="M1 1l3.5 3.5L8 1" stroke="#3d55a8" fill="none"/></svg></div>

<aside class="abs panel sidebar">
  <div class="sidebar-head">Recommended for you:</div>
  <div class="rec" style="top:47px"><div class="ph" style="background:linear-gradient(#6d5a4b,#a97f76)" role="img" aria-label="Baby with a large snake"></div><h3>Article title will be here in lines.</h3><div class="meta"><span>Admin Name</span><span>|</span><span>1 day ago</span><span>|</span><span>99 comments</span></div></div>
  <div class="rec" style="top:240px"><div class="ph" style="background:linear-gradient(#6c6c6c,#c9c9c9)" role="img" aria-label="Giant ball on a car"></div><h3>Article title will be here in lines.</h3><div class="meta"><span>Admin Name</span><span>|</span><span>1 day ago</span><span>|</span><span>99 comments</span></div></div>
  <div class="rec" style="top:429px"><div class="ph" style="background:linear-gradient(#6b4a63,#d9b8a4)" role="img" aria-label="Makeup portrait"></div><h3>Article title will be here in lines.</h3><div class="meta"><span>Admin Name</span><span>|</span><span>1 day ago</span><span>|</span><span>99 comments</span></div></div>
  <div class="rec" style="top:619px"><div class="ph" style="background:linear-gradient(#dcdcdc,#4a4a4a)" role="img" aria-label="Black and white disguise portraits"></div><h3>Article title will be here in lines.</h3><div class="meta"><span>Admin Name</span><span>|</span><span>1 day ago</span><span>|</span><span>99 comments</span></div></div>
</aside>

<section class="abs newsletter">
  <h4>GET MORE VIRAL IN YOUR INBOX!</h4>
  <p>Sign up for our daily email newsletter for free<br>and get updated</p>
  <div class="field">Your email here</div>
  <div class="submit">Submit</div>
</section>

<footer class="abs footer">
  <div><span>About</span><span>RSS</span><span>Privacy</span><span>Contact</span><span>Copyright</span></div>
  <div>© 2016. All rights reserved.</div>
</footer>
</body>
</html>
```